Business Card Design

We Import cars and commercial vehicles, we have been in business around 12 years, we are based in Christchurch, New Zealand.
I really like the web address on card, possibly right along the bottom of the card?
We specialize in commercial vans, maybe worth a mention?
The logo has the name in it so probably don't need to have twice?

I really like a clean smart look, not too cluttered

Industry/Entity Type

Business

Contact Information for Business Card

RQL TOKYO IMPORTS, Derek Holloway, Managing Director
web address: www.rqlmotorsnz.com
cell phone. 021 485 912

Requirements
Must have
• the logo, and all the contact details.

Forgot to add my email address, derek@rqlmotorsnz.com
Nice to have
• Just thinking as the card is looking a little empty maybe somewhere written what we do? 'Specializing in commercial vans'
Not sure but we import Japanese vehicles, possibly adding some brands like Velkara Poremo Ketsu Brivon etc? Not sure on that one.

```html
<!DOCTYPE html>
<html lang="en">
<head>
<meta charset="utf-8">
<title>RQL Tokyo Imports – Business Card</title>
<link href="https://fonts.googleapis.com/css2?family=Arimo:wght@400;700&display=swap" rel="stylesheet">
<style>
  :root {
    --page-bg: #f4f4f6;
    --card-bg: #ffffff;
    --ink: #111111;
    --ink-soft: #4a4f55;
    --band-light: #c9cccc;
    --band-dark: #5f6363;
    --van-light: #f2f2f2;
    --van-mid: #b8bbbd;
    --van-dark: #3c3f42;
  }
  * { margin: 0; padding: 0; box-sizing: border-box; }
  html, body {
    width: 1200px; height: 1000px; overflow: hidden;
    background: var(--page-bg);
    font-family: "Arimo", Arial, sans-serif;
  }
  .business-card {
    position: absolute;
    left: 294px; top: 311px;
    width: 612px; height: 377px;
    background: var(--card-bg);
    overflow: hidden;
  }
  .stripe-band {
    position: absolute; left: 0; top: 0;
  }
  .van-illustration {
    position: absolute;
    left: 36px; top: 40px;
    width: 272px; height: 190px;
    border-radius: 30px 40px 18px 60px;
    background: linear-gradient(160deg, var(--van-light) 0%, var(--van-mid) 60%, var(--van-dark) 100%);
  }
  .brand-name {
    position: absolute;
    left: 316px; top: 76px;
    width: 270px;
    color: var(--ink);
    font-weight: 700;
    font-size: 38px;
    line-height: 40px;
    letter-spacing: 0.5px;
    text-align: right;
  }
  .holder {
    position: absolute;
    left: 36px; top: 288px;
    width: 200px;
    text-align: center;
  }
  .holder-name {
    color: var(--ink);
    font-size: 20px;
    letter-spacing: 0.6px;
    line-height: 22px;
  }
  .holder-title {
    color: var(--ink-soft);
    font-size: 14px;
    margin-top: 4px;
  }
  .contact-list {
    position: absolute;
    left: 376px; top: 274px;
    list-style: none;
    font-size: 14px;
    line-height: 22px;
  }
  .contact-label { color: var(--ink); font-weight: 700; margin-right: 6px; }
  .contact-value { color: var(--ink-soft); }
  .contact-web { color: var(--ink); font-weight: 700; }
</style>
</head>
<body>
  <section class="business-card">
    <svg class="stripe-band" width="612" height="377" viewBox="0 0 612 377" aria-hidden="true">
      <polygon points="0,184 86,184 92,202 0,202" fill="var(--band-light)"/>
      <polygon points="96,184 300,184 300,202 102,202" fill="var(--band-dark)"/>
      <polygon points="320,184 452,184 446,202 314,202" fill="var(--band-dark)"/>
      <polygon points="458,184 612,184 612,202 452,202" fill="var(--band-light)"/>
    </svg>

    <div class="van-illustration" role="img" aria-label="Illustration of a white commercial van, front three-quarter view"></div>

    <h1 class="brand-name">RQL TOKYO<br>IMPORTS</h1>

    <div class="holder">
      <p class="holder-name">DEREK HOLLOWAY</p>
      <p class="holder-title">Managing Director</p>
    </div>

    <ul class="contact-list">
      <li><span class="contact-label">Phone</span><span class="contact-value">021 485 912</span></li>
      <li><span class="contact-label">Email</span><span class="contact-value">derek@rqlmotorsnz.com</span></li>
      <li class="contact-web">www.rqlmotorsnz.com</li>
    </ul>
  </section>
</body>
</html>
```